Media Browser and player web application

I need to redesign a web application that enables to browse a media server (Tellavo) contents (images, audio, video) and play it in a web player.

Current implementation of the application can be seen at: http://www.tellavohub.example/content/demonstration-tellavo-pro-online-media-browser

This refresh is aiming to:
1) make the application simpler, based on typology (think Windows Metro style, VidSpire, Flickora); a simple fan concept is here: http://dex.lomarquin.example/tellavo/
2) make the application work on desktop as well as touch screen devices (ie no hover functionality, no pagination, large touch controls)
3) fast (remove unnecessary animations)
4) design with the app being responsive in mind

The attached UX designs show the basic flows in the application. Please note that the placement of controls (for example) is not set in stone and I welcome your input on the layout.

Ideally the default theme will be dark. Items' thumbnails will be square place holders, with images fit in them depending on the item icons' aspect ratio.

Also attaching the product's logo (Tellavo) and icon. The web application's name is ClipRover (or Tellavo ClipRover), so it should be included in the design (the UX designs include place holder Tellavo logo in the left top corner).

The main categories for each file type are (you will have to provide an icon for each of these):
- Audio: Albums, Artists, Album artists, Folders, Genres, Composers, Titles, Random music, Random albums, Last listened, Playlists, Online
- Image: Albums, Folders, Year, Month, Playlists, Online
- Video: Titles, Movies, Series, Folders, Last viewed, Last added, Genres, Actors, Directors, Producers, Release years, Playlists, Online
Updates

Target Market(s)

Mostly tech enthusiasts who want to stream their media over the internet to their devices.

Industry/Entity Type

Artists

Requirements
Must have
• Designs for all the provided UX designs
Touch-friendly web application design
High-res (Retina) assets
Light, type based Metro-like design
Nice to have
• Responsive web version
Dark and Light theme switching.
Should not have
• Chrome
Heavy graphics (eg backgrounds) that take time to load

```html
<!DOCTYPE html>
<html lang="en">
<head>
<meta charset="utf-8">
<title>Tellavo ClipRover</title>
<link rel="stylesheet" href="https://fonts.googleapis.com/css2?family=Raleway:wght@500;700&display=swap">
<style>
  :root {
    --bg-center: #2b5878;
    --bg-edge: #0d2c4c;
    --tile: #3898dc;
    --tab: #268fc6;
    --tab-edge: #175f98;
    --brand: #0a9be0;
    --brand-edge: #23374a;
    --ribbon: rgba(39, 160, 220, 0.55);
    --ribbon-soft: rgba(39, 160, 220, 0);
    --ink: #ffffff;
  }
  html, body { margin: 0; padding: 0; overflow: hidden; }
  .canvas {
    position: relative;
    width: 1200px;
    height: 1000px;
    overflow: hidden;
    background: radial-gradient(ellipse 60% 75% at 50% 50%, var(--bg-center) 0%, #24506f 55%, var(--bg-edge) 100%);
    font-family: "Raleway", sans-serif;
  }
  .ribbon-art {
    position: absolute;
    border-radius: 50%;
    background: radial-gradient(ellipse at center, var(--ribbon) 0%, var(--ribbon-soft) 70%);
  }
  .ribbon-art--top { left: 660px; top: -60px; width: 360px; height: 460px; }
  .ribbon-art--bottom { left: 140px; top: 630px; width: 400px; height: 440px; }
  .brand-panel { position: absolute; left: 0; top: 0; width: 400px; height: 190px; }
  .brand-panel svg { position: absolute; inset: 0; }
  .brand-name {
    position: absolute;
    left: 100px;
    top: 20px;
    margin: 0;
    font-size: 34px;
    font-weight: 700;
    line-height: 38px;
    color: var(--ink);
  }
  .categories {
    position: absolute;
    top: 398px;
    left: 152px;
    display: flex;
    gap: 19px;
  }
  .category {
    position: relative;
    width: 284px;
    height: 219px;
    background: var(--tile);
  }
  .category svg { position: absolute; inset: 0; }
  .category-label {
    position: absolute;
    left: 82px;
    top: 186px;
    width: 120px;
    height: 62px;
    background: var(--tab);
    border-bottom: 5px solid var(--tab-edge);
    color: var(--ink);
    font-size: 17px;
    font-weight: 500;
    line-height: 66px;
    text-align: center;
  }
</style>
</head>
<body>
<div class="canvas">
  <div class="ribbon-art ribbon-art--top" role="img" aria-label="Decorative folded ribbon illustration"></div>
  <div class="ribbon-art ribbon-art--bottom" role="img" aria-label="Decorative folded ribbon illustration"></div>

  <header class="brand-panel">
    <svg width="400" height="190" viewBox="0 0 400 190" aria-hidden="true">
      <polygon points="355,0 378,0 355,173 332,167" fill="var(--brand-edge)"/>
      <polygon points="78,0 355,0 332,167 80,98" fill="var(--brand)"/>
    </svg>
    <p class="brand-name">Tellavo<br>ClipRover</p>
  </header>

  <nav class="categories">
    <div class="category">
      <svg width="284" height="219" viewBox="0 0 284 219" aria-hidden="true">
        <rect x="79" y="39" width="26" height="16" fill="#fff"/>
        <rect x="61" y="52" width="158" height="103" rx="12" fill="#fff"/>
        <rect x="171" y="63" width="34" height="15" fill="var(--tile)"/>
        <circle cx="141" cy="104" r="32" fill="none" stroke="var(--tile)" stroke-width="7"/>
        <circle cx="141" cy="104" r="10" fill="var(--tile)"/>
      </svg>
      <div class="category-label">IMAGE</div>
    </div>
    <div class="category">
      <svg width="284" height="219" viewBox="0 0 284 219" aria-hidden="true">
        <rect x="96" y="89" width="102" height="66" rx="3" fill="#fff"/>
        <g fill="var(--tile)">
          <polygon points="100,92 112,92 120,105 108,105"/>
          <polygon points="128,92 140,92 148,105 136,105"/>
          <polygon points="156,92 168,92 176,105 164,105"/>
        </g>
        <g transform="rotate(-27 94 80)">
          <rect x="88" y="68" width="100" height="14" rx="3" fill="#fff"/>
          <g fill="var(--tile)">
            <polygon points="100,71 110,71 116,79 106,79"/>
            <polygon points="126,71 136,71 142,79 132,79"/>
            <polygon points="152,71 162,71 168,79 158,79"/>
          </g>
        </g>
      </svg>
      <div class="category-label">VIDEO</div>
    </div>
    <div class="category">
      <svg width="284" height="219" viewBox="0 0 284 219" aria-hidden="true">
        <path d="M76,125 V112 A66,66 0 0 1 208,112 V125" fill="none" stroke="#fff" stroke-width="11"/>
        <rect x="67" y="110" width="24" height="46" rx="10" fill="#fff"/>
        <rect x="99" y="110" width="8" height="44" rx="4" fill="#fff"/>
        <rect x="193" y="110" width="24" height="46" rx="10" fill="#fff"/>
        <rect x="177" y="110" width="8" height="44" rx="4" fill="#fff"/>
      </svg>
      <div class="category-label">AUDIO</div>
    </div>
  </nav>
</div>
</body>
</html>
```